We need a letterhead incorporating our logo (uploaded file), with the name of our organization (Dunmore Hollis County Police Association) and our slogan (Together We Serve). Dark blue should be incorporated somewhere in the design, either the font color or elsewhere. Please make sure our logo is included in the design. The organization is a law enforcement union type group.

Target Market(s)

Members of our association, policticians, and anyone receiving our letters

Colors
0255a3

Requirements
Must have
• Our logo, Association name, and slogan.
Nice to have
• A professional and eye-catching letterhead design incorporating the logo, name, and slogan.

```html
<!DOCTYPE html>
<html lang="en">
<head>
<meta charset="utf-8">
<title>Dunmore Hollis County Police Association — Letterhead</title>
<link rel="stylesheet" href="https://fonts.googleapis.com/css2?family=Arimo:wght@400;700&display=swap">
<style>
  :root {
    --backdrop: #e6e6e6;
    --paper: #ffffff;
    --navy: #0f1c3d;
    --navy-mid: #1b2d5a;
    --navy-light: #3a5089;
    --brand-blue: #0255a3;
    --ink: #111111;
    --watermark: #eef4fb;
  }
  html, body {
    margin: 0;
    padding: 0;
    width: 1200px;
    height: 873px;
    overflow: hidden;
    background: var(--backdrop);
  }
  .letterhead {
    position: absolute;
    left: 278px;
    top: 20px;
    width: 644px;
    height: 833px;
    box-shadow: 0 4px 18px rgba(0,0,0,0.25);
  }
  .org-name {
    font-family: "Arimo", Arial, sans-serif;
    font-weight: 700;
    fill: var(--navy);
  }
  .tagline {
    font-family: "Arimo", Arial, sans-serif;
    font-weight: 400;
    letter-spacing: 3px;
    fill: var(--brand-blue);
  }
  .letter-heading {
    font-family: "Arimo", Arial, sans-serif;
    font-weight: 700;
    fill: var(--ink);
  }
  .letter-body {
    font-family: "Arimo", Arial, sans-serif;
    font-weight: 400;
    fill: var(--ink);
  }
</style>
</head>
<body>
<svg class="letterhead" viewBox="0 0 1016 1314" xmlns="http://www.w3.org/2000/svg" aria-label="Association letterhead">
  <defs>
    <linearGradient id="swoosh-sheen" x1="0" y1="0" x2="1" y2="1">
      <stop offset="0" stop-color="var(--navy)"/>
      <stop offset="0.6" stop-color="var(--navy-mid)"/>
      <stop offset="1" stop-color="var(--navy-light)"/>
    </linearGradient>
    <linearGradient id="footer-band" x1="0" y1="0" x2="1" y2="0">
      <stop offset="0" stop-color="var(--navy-mid)"/>
      <stop offset="0.5" stop-color="var(--navy)"/>
      <stop offset="1" stop-color="var(--navy-light)"/>
    </linearGradient>
  </defs>

  <rect class="sheet" width="1016" height="1314" fill="var(--paper)"/>

  <circle class="background-disc" cx="513" cy="728" r="360" fill="var(--watermark)"/>

  <g class="header-swoosh">
    <path d="M450,0 C690,40 880,140 1016,268 L1016,0 Z" fill="url(#swoosh-sheen)"/>
    <path d="M640,0 C780,40 920,130 1016,236 L1016,250 C915,145 770,52 620,0 Z" fill="var(--paper)"/>
    <path d="M880,0 C940,50 985,110 1016,160 L1016,100 C995,60 965,25 935,0 Z" fill="var(--navy-light)" opacity="0.55"/>
  </g>

  <circle class="brand-dot" cx="160" cy="145" r="80" fill="var(--brand-blue)"/>

  <text class="org-name" x="275" y="128" font-size="28">DUNMORE HOLLIS COUNTY</text>
  <text class="org-name" x="275" y="168" font-size="32">POLICE ASSOCIATION</text>
  <line class="rule" x1="275" y1="190" x2="640" y2="190" stroke="var(--brand-blue)" stroke-width="2"/>
  <text class="tagline" x="275" y="220" font-size="17">TOGETHER WE SERVE</text>

  <text class="letter-heading" x="171" y="384" font-size="17.5">LOREM IPSUM DOLOR SIT</text>
  <g class="letter-body" font-size="15.5">
    <text x="173" y="462">LOREM IPSUM DOLOR SIT AMET, CONSECTETUER ADIPISCING ELIT, SED DIAM</text>
    <text x="173" y="518">NONUMMY NIBH EUISMOD TINCIDUNT UT LAOREET DOLORE MAGNA ALIQUAM ERAT</text>
    <text x="173" y="573">VOLUTPAT. UT WISI ENIM AD MINIM VENIAM, QUIS NOSTRUD EXERCI TATION ULLAM-</text>
    <text x="173" y="629">CORPER SUSCIPIT LOBORTIS NISL UT ALIQUIP EX EA COMMODO CONSEQUAT. DUIS</text>
    <text x="173" y="684">AUTEM VEL EUM IRIURE DOLOR IN HENDRERIT IN VULPUTATE VELIT ESSE MOLESTIE</text>
    <text x="173" y="740">CONSEQUAT.</text>
    <text x="173" y="851">LOREM IPSUM DOLOR SIT AMET, CONS ECTETUER ADIPISCING ELIT, SED DIAM</text>
    <text x="173" y="907">NONUMMY NIBH EUISMOD TINCIDUNT UT LAOREET DOLORE MAGNA ALIQUAM ERAT</text>
    <text x="173" y="962">VOLUTPAT. UT WISI ENIM AD MINIM VENIAM, QUIS NOSTRUD EXERCI TATION ULLAM-</text>
    <text x="173" y="1018">CORPER SUSCIPIT LOBORTIS NISL UT ALIQUIP EX EA COMMODO CONSEQUAT.</text>
  </g>

  <g class="footer-band">
    <rect x="0" y="1270" width="1016" height="44" fill="url(#footer-band)"/>
    <path d="M100,1314 L160,1270 L240,1270 L180,1314 Z" fill="var(--navy-light)" opacity="0.5"/>
    <path d="M420,1314 L480,1270 L520,1270 L460,1314 Z" fill="var(--navy-light)" opacity="0.4"/>
    <path d="M700,1270 L780,1270 L850,1314 L770,1314 Z" fill="var(--navy-light)" opacity="0.45"/>
    <path d="M900,1314 L960,1270 L1016,1270 L1016,1290 L990,1314 Z" fill="var(--navy-light)" opacity="0.5"/>
  </g>
</svg>
</body>
</html>
```